"Lantern Field" Play - Poster Design for Theatre Group

We are an amateur theatre group based in Geneva, Switzerland. We take pride in eye-catching posters for our shows, which are printed in various sizes.
This design will be for a play in March 2016. The play is called "Lantern Field", and it's a Harwick Medal winner from Marcus Ellery-Pound. The play is about a couple who have everything a family could want, until they lose a child in a life-shattering accident that turns their world upside down. The play charts the couple's bittersweet search to find each other and to find comfort.
Most importantly, we want a design that will make people want to see the show. We don't want to give away the plot or be too heavy-handed about death, but we want it to be clear that it's not a comedy (although there are some lighter moments!).
Attached you will find a template for the poster. This simply has our group name and logo in the top right corner: (Lakeshore Stage Players Circle presents).
You may change the color of both the text and the logo, but please do not change the font, size, or location.
Here is the information that needs to be on the poster, wherever you see fit:
play title: Lantern Field
author byline: by Marcus Ellery-Pound
director line: directed by Rob Feltwick
tagline: How do you keep it together when your whole world's fallen apart?
dates and times:
1-5 March 2016
(Tue-Fri 20:00, Sat 19:00)
location:
Théâtre du Vieux-Moulin
Eaux-Vives, Geneva
websites:
www.lspc.ch
www.scenelettres.ch
Technical Details:
Any font or combination of fonts is acceptable. The largest text should be the play title. The author's name must be at least 50% of the title font size.
For this competition, we would like the version with A3 proportions, which will also be used at F4 (89.5 x 128 cm) and A5 sizes (14.8 x 21 cm). Therefore no text should be below 9pt at A5.
However, from the winning designer we will also need repurposed sizes of the same design. Here is a comprehensive list of the sizes we will need.
1) A3 print poster. Artwork should be 300dpi, CMYK, sent with a 1mm bleed all round, to specification PDF/X-1A:2001. We will need this image in PDF format in addition to the default Artbrigade formats.
2) Chatterly advert picture. 1200px by 628px, RGB jpeg. This must comply with Chatterly’s restrictions on amount of text, which is no more than 20% of area taken up by text.(https://www.chatterly.example/ads/tools/text_overlay).
Because of these restrictions it is sufficient to include just the title and the author's name in this version.
3) Chatterly cover picture: 851px by 314px. RGB jpeg. It is sufficient to include just the title and the author's name in this version.
4) Web banner. 1000px by 300px. RGB jpeg. This version should include just the main image(s), no text.
Theatergoers
Entertainment

```html
<!DOCTYPE html>
<html lang="en">
<head>
<meta charset="utf-8">
<title>Lantern Field – Poster</title>
<link rel="stylesheet" href="https://fonts.googleapis.com/css2?family=Quicksand:wght@400&family=Fjalla+One&family=Cutive+Mono&display=swap">
<style>
  :root {
    --page: #ffffff;
    --rust: #9a4d0c;
    --ink: #23282b;
    --title: #d8d5d4;
    --cream: #f4e8cc;
    --ember: #8b0000;
  }
  * { margin: 0; padding: 0; box-sizing: border-box; }
  html, body { width: 1200px; height: 1200px; overflow: hidden; background: var(--page); }
  .poster {
    position: absolute; left: 202px; top: 38px;
    width: 790px; height: 1114px;
    background: var(--rust); overflow: hidden;
  }
  .poster > * { position: absolute; }
  .artwork { left: 0; top: 0; width: 790px; height: 1114px; }
  .presenter {
    right: 144px; top: 30px;
    font-family: "Fjalla One", sans-serif; font-size: 23px; line-height: 29px;
    color: var(--cream); text-align: right;
  }
  .presenter-mark {
    left: 670px; top: 26px; width: 96px; height: 96px;
    border: 2px solid var(--cream); border-radius: 50%;
  }
  .tagline {
    left: 12px; top: 152px; width: 770px;
    font-family: "Cutive Mono", monospace; font-size: 18px;
    letter-spacing: 0.6px; color: var(--cream); white-space: nowrap;
  }
  .title-art { left: 0; top: 0; width: 790px; height: 1114px; }
  .title-text, .byline-text {
    font-family: "Quicksand", sans-serif; font-weight: 400; fill: var(--title);
  }
  .title-disc { fill: var(--ember); }
  .director {
    right: 66px; top: 921px;
    font-family: "Fjalla One", sans-serif; font-size: 29px; color: var(--title);
  }
  .details {
    top: 1024px; font-family: "Fjalla One", sans-serif;
    font-size: 19px; line-height: 25px; color: var(--title); white-space: pre;
  }
  .details-when { left: 28px; }
  .details-web { left: 518px; }
</style>
</head>
<body>
  <main class="poster">
    <svg class="artwork" viewBox="0 0 790 1114" role="img" aria-label="Splattered paint burst fading from rust orange into dark charcoal around the title">
      <defs>
        <linearGradient id="rust-to-ink" x1="0" y1="0" x2="0" y2="1">
          <stop offset="0" stop-color="#9a4d0c"/>
          <stop offset="0.42" stop-color="#9a4d0c"/>
          <stop offset="0.56" stop-color="#5a4030"/>
          <stop offset="0.66" stop-color="#23282b"/>
          <stop offset="1" stop-color="#23282b"/>
        </linearGradient>
      </defs>
      <rect width="790" height="1114" fill="url(#rust-to-ink)"/>
    </svg>

    <div class="presenter">Lakeshore Stage<br>Players Circle<br>presents</div>
    <div class="presenter-mark" aria-hidden="true"></div>

    <p class="tagline">How do you keep it together when your whole world's fallen apart?</p>

    <svg class="title-art" viewBox="0 0 790 1114" role="img" aria-label="Lantern Field by Marcus Ellery-Pound">
      <text class="title-text" x="102" y="414" font-size="200" textLength="640" lengthAdjust="spacingAndGlyphs">Lantern</text>
      <circle class="title-disc" cx="360" cy="621" r="44"/>
      <g class="title-text" font-size="200" text-anchor="middle">
        <text class="title-text" x="160" y="674">F</text>
        <text class="title-text" x="262" y="674">i</text>
        <text class="title-text" x="360" y="674">e</text>
        <text class="title-text" x="452" y="674">l</text>
        <text class="title-text" x="540" y="674">d</text>
      </g>
      <text class="byline-text" x="102" y="885" font-size="58" textLength="620" lengthAdjust="spacingAndGlyphs">by Marcus Ellery-Pound</text>
    </svg>

    <p class="director">directed by Rob Feltwick</p>

    <p class="details details-when">1-5 March 2016     (Tue-Fri 20:00, Sat 19:00)
Théâtre du Vieux-Moulin Eaux-Vives, Geneva</p>
    <p class="details details-web">www.lspc.ch
www.scenelettres.ch</p>
  </main>
</body>
</html>
```